Ironvale Beard Oil - Premium Label Design

We need a premium, masculine, and minimalistic label design for our new beard oil brand, Ironvale. The product is crafted with grass-fed beef tallow and essential oils. The design should evoke strength, authenticity, and sophistication, without being too busy. We want a bold, clean look, with the slogan integrated:
“Be the Monument. Crafted with Beef Tallow. Forged for Men.”
Please make sure the style is modern and rugged, possibly featuring a monolithic stone element in the background, similar to the inspiration provided in the uploaded file but it need to be sorta completely different.
Updates
I want the label to be able to fit the type of bottle matte black
Industry/Entity Type
Skin Care
Colors
Designer to choose colors to be used in the design.
Requirements
Must have
- Back and front. Creative IRONVALE police design, Beard oil and aftershave mentioned
Nice to have
- grass fed icon, bio icon

```html
<!DOCTYPE html>
<html lang="en">
<head>
<meta charset="utf-8">
<title>Ironvale Beard Oil – Label and Carton</title>
<link rel="stylesheet" href="https://fonts.googleapis.com/css2?family=Josefin+Sans:wght@400;600;700&display=swap">
<style>
  :root {
    --stage: #0b0b0b;
    --ink-dark: #1c1c1c;
    --ink-light: #f1f1f1;
    --mist-top: #9a9a9a;
    --mist-mid: #b9b9b9;
    --mist-low: #5e5e5e;
    --carton: #4a4a4a;
    --carton-low: #3a3a3a;
    --badge: #cfcfcf;
  }
  * { box-sizing: border-box; margin: 0; padding: 0; }
  html, body {
    width: 1200px; height: 800px; overflow: hidden;
    background: var(--stage);
    font-family: "Josefin Sans", sans-serif;
  }
  .stage { position: relative; width: 1200px; height: 800px; }

  /* Front label */
  .front-label {
    position: absolute; left: 400px; top: 220px;
    width: 220px; height: 300px; overflow: hidden;
  }
  .label-scene {
    position: absolute; inset: 0;
    background:
      linear-gradient(90deg, rgba(40,40,40,.75) 0 12%, transparent 16%),
      linear-gradient(180deg, var(--mist-top) 0%, var(--mist-mid) 55%, var(--mist-low) 85%, #3a3a3a 100%);
  }
  .label-content {
    position: absolute; inset: 0;
    display: flex; flex-direction: column; align-items: center;
    padding-top: 132px; text-align: center;
  }
  .brand-name {
    font-weight: 700; font-size: 33px; letter-spacing: 1px;
    color: var(--ink-dark); line-height: 1;
  }
  .product-type {
    font-weight: 400; font-size: 10px; letter-spacing: 4px;
    color: var(--ink-dark); margin-top: 4px;
  }
  .slogan {
    margin-top: 16px; color: var(--ink-light);
    font-size: 13px; line-height: 19px; font-weight: 400;
  }
  .bio-badge {
    position: absolute; right: 10px; bottom: 12px;
    width: 14px; height: 14px; border-radius: 50%;
    background: var(--badge);
  }

  /* Carton front panel */
  .carton-panel {
    position: absolute; left: 650px; top: 130px;
    width: 170px; height: 500px; overflow: hidden;
  }
  .carton-scene {
    position: absolute; inset: 0;
    background:
      linear-gradient(180deg, var(--carton) 0%, #5a5a5a 55%, var(--carton-low) 82%, #2b2b2b 100%);
  }
  .carton-wordmark {
    position: absolute; left: 50%; top: 255px;
    transform: translate(-50%, -50%) rotate(-90deg);
    display: flex; flex-direction: column; align-items: center;
    white-space: nowrap;
  }
  .carton-wordmark .brand-name { font-size: 62px; color: #1a1a1a; }
  .carton-wordmark .product-type { font-size: 17px; letter-spacing: 7px; color: #1f1f1f; margin-top: 6px; }
  .carton-panel .bio-badge { right: 12px; bottom: 14px; width: 16px; height: 16px; background: #9a9a9a; }
</style>
</head>
<body>
  <main class="stage">
    <section class="front-label">
      <div class="label-scene" role="img" aria-label="Misty grey landscape with a tall weathered stone monolith on the left"></div>
      <div class="label-content">
        <h1 class="brand-name">IRONVALE</h1>
        <p class="product-type">BEARD OIL</p>
        <p class="slogan">Be the Monument<br>Crafted with Beef Tallow<br>Forged for Men</p>
      </div>
      <span class="bio-badge"></span>
    </section>

    <section class="carton-panel">
      <div class="carton-scene" role="img" aria-label="Dim grey stone ground and fog behind the carton lettering"></div>
      <div class="carton-wordmark">
        <h2 class="brand-name">IRONVALE</h2>
        <p class="product-type">BEARD OIL</p>
      </div>
      <span class="bio-badge"></span>
    </section>
  </main>
</body>
</html>
```